Lucky Orbit Fun Casino Entertainment

Looking to update my business card and make it look more modern, stand out and eye catching.
We are are fun casino business in Australia (primarily Sydney). Blackjack and Roulette are our most popular games although we have pretty much every game available for hire that you would find in a real casino. The final design would need to be sleek and appeal to the more upmarket corporate sector.
We mainly cater for Corporate Events, Private Parties, Fundraising Events, Team Building, Poker Tournaments
I think I'd prefer the colour Black.

Target Market(s)

High-end Corporate

Industry/Entity Type

Events

Contact Information for Business Card

Dale Hutchins
Director
1300 482 617
0431 758 209
info@luckyorbit.com.au
www.luckyorbit.com.au
Facebook & Instagram @luckyorbitshows (proper social icons preferred)

Colors
000000
0255a3

Requirements
Must have
• Front side:
• Logo
• Contact details
• 'Australia's #1 Fun Casino Specialists'
• Back:
• Logo
Nice to have
• Back:
• Corporate Events
• Private Parties
• Poker Tournaments
• Fundraising
• Props & Theming
• Photo Booth
• Horse Racing Events
• The Vegas Sign attached, maybe on the back of the card in the background...?

```html
<!DOCTYPE html>
<html lang="en">
<head>
<meta charset="utf-8">
<title>Lucky Orbit Business Card</title>
<link rel="stylesheet" href="https://fonts.googleapis.com/css2?family=Playfair+Display:wght@400;700&display=swap">
<style>
  :root {
    --backdrop: #3a3a3c;
    --card-black: #0c0c0c;
    --card-edge: #1a1a1a;
    --gold: #f2a91f;
    --gold-soft: #d8951a;
    --sign-light: #fbe7a6;
    --sign-mid: #e9b949;
    --sign-deep: #b77a1a;
  }
  * { margin: 0; padding: 0; box-sizing: border-box; }
  html, body {
    width: 1200px; height: 900px; overflow: hidden;
    background: var(--backdrop);
    font-family: "Playfair Display", Georgia, serif;
  }
  .canvas {
    width: 1200px; height: 900px;
    display: flex; align-items: center; justify-content: center; gap: 50px;
  }
  .card {
    position: relative;
    width: 540px; height: 309px;
    background: radial-gradient(ellipse at 50% 40%, var(--card-edge), var(--card-black) 75%);
    color: var(--gold);
    overflow: hidden;
    box-shadow: 0 14px 34px rgba(0,0,0,0.45);
  }

  /* Front side */
  .card-front {
    display: flex; flex-direction: column; align-items: center;
    padding-top: 52px; text-align: center;
  }
  .brand-mark {
    display: flex; align-items: center; gap: 10px;
    font-size: 26px; font-weight: 700; letter-spacing: 1px;
    color: var(--gold);
  }
  .brand-mark .dot {
    width: 22px; height: 22px; border-radius: 50%;
    background: var(--gold);
  }
  .person-name {
    margin-top: 30px;
    font-size: 21px; font-weight: 700; letter-spacing: 1px;
  }
  .person-role { font-size: 14px; margin-top: 2px; }
  .contact-line {
    font-size: 14px; margin-top: 10px; color: var(--gold-soft);
  }
  .contact-line + .contact-line { margin-top: 5px; }
  .sep { margin: 0 8px; }
  .social {
    display: inline-flex; align-items: center; gap: 6px;
  }
  .social .dot {
    width: 9px; height: 9px; border-radius: 50%; background: var(--gold-soft);
  }

  /* Back side */
  .sign-photo {
    position: absolute; left: 0; top: 0;
    width: 300px; height: 175px;
  }
  .back-text {
    position: absolute; right: 30px; top: 40px;
    text-align: right;
  }
  .tagline { font-size: 17px; line-height: 1.2; }
  .tagline .big { font-size: 26px; font-weight: 700; }
  .back-brand {
    margin-top: 8px;
    font-size: 30px; font-weight: 700; letter-spacing: 2px;
  }
  .services {
    list-style: none; margin-top: 12px;
    font-size: 14.5px; line-height: 1.5;
  }
</style>
</head>
<body>
<main class="canvas">

  <section class="card card-front" aria-label="Card front">
    <div class="brand-mark"><span class="dot"></span>LUCKY ORBIT</div>
    <p class="person-name">DALE HUTCHINS</p>
    <p class="person-role">Director</p>
    <p class="contact-line">1300 482 617<span class="sep">|</span>0431 758 209</p>
    <p class="contact-line">info@luckyorbit.com.au<span class="sep">|</span>www.luckyorbit.com.au</p>
    <p class="contact-line"><span class="social"><span class="dot"></span>@luckyorbitshows</span></p>
  </section>

  <section class="card card-back" aria-label="Card back">
    <svg class="sign-photo" viewBox="0 0 300 175" role="img" aria-label="Photo of the famous welcome sign of a casino city, peeled back from the corner">
      <defs>
        <linearGradient id="signGlow" x1="0" y1="0" x2="1" y2="1">
          <stop offset="0" stop-color="var(--sign-light)"/>
          <stop offset="0.55" stop-color="var(--sign-mid)"/>
          <stop offset="1" stop-color="var(--sign-deep)"/>
        </linearGradient>
      </defs>
      <path d="M0 0 H300 Q250 90 215 175 H0 Z" fill="url(#signGlow)"/>
      <path d="M300 0 Q250 90 215 175" fill="none" stroke="var(--gold)" stroke-width="6"/>
    </svg>
    <div class="back-text">
      <p class="tagline">Australia's #1<br>Fun <span class="big">Casino</span> Specialists</p>
      <p class="back-brand">LUCKY ORBIT</p>
      <ul class="services">
        <li>Corporate Events | Private Parties</li>
        <li>Poker Tournaments | Fundraising</li>
        <li>Props &amp; Theming | Photo Booth</li>
        <li>Horse Racing Events</li>
      </ul>
    </div>
  </section>

</main>
</body>
</html>
```